Insect farm business card BUGS BUGS BUGS!

Looking for a unique double sided business card design to reflect our unique business!

We run a bug farm and have 4 separate websites for different arms of our business.

I would love to have an amazing business card design that incorporates all of these components (so that they look like they belong together).

The 4 websites are

wingmeadowlane.com.au Live butterflies for release.

Critterden.com.au Educational insect life cycle kits and school presentations all about bugs

theamberlocust.com.au tarantulas, scorpions, stick insects as pets

crunchypantryfare.com.au insect you can eat and heaps of edible insect products.

I don't need a description for each website, but do need the design to reflect all of the aspects.

We are an Australian company, and only breed native Australian invertebrates. Please do not include images of non Australia species (eg red kneed tarantulas, emperor scorpions etc).

I will include some images of Australian invertebrates. Feel free to use these if you like, or you can use other images if this suits you better.

Please include 4 website addresses, email, phone and name

• Integrate components of all 4 websites.
• No images of non Australian invertebrate species

```html
<!DOCTYPE html>
<html lang="en">
<head>
<meta charset="utf-8">
<title>Bug Farm Business Card</title>
<link rel="stylesheet" href="https://fonts.googleapis.com/css2?family=Baloo+2:wght@700&family=Comfortaa:wght@400;700&display=swap">
<style>
  :root {
    --bg: #e4e4e6;
    --card: #ffffff;
    --yellow: #e6b61e;
    --leaf-green: #6cbf4a;
    --blue: #2d5db3;
    --forest: #2e7a3a;
    --brown: #7b4a1c;
    --shadow: rgba(0,0,0,0.14);
  }
  * { box-sizing: border-box; margin: 0; padding: 0; }
  html, body { width: 900px; height: 1200px; overflow: hidden; background: var(--bg); }
  .canvas { position: relative; width: 900px; height: 1200px; }

  .card {
    position: absolute; left: 140px; width: 620px; height: 354px;
    background: var(--card); overflow: hidden;
    box-shadow: 0 6px 18px var(--shadow);
  }
  .card--front { top: 150px; }
  .card--back { top: 696px; }

  /* Front */
  .bugs-word {
    position: absolute; font-family: "Baloo 2", "Arial Rounded MT Bold", sans-serif;
    font-weight: 700; font-size: 92px; line-height: 1; letter-spacing: 2px;
    white-space: nowrap;
  }
  .bugs-word--forest { color: var(--forest); left: 290px; top: 2px; }
  .bugs-word--blue   { color: var(--blue);   left: 150px; top: 88px; }
  .bugs-word--green  { color: var(--leaf-green); left: 300px; top: 174px; }
  .bugs-word--yellow { color: var(--yellow); left: 40px;  top: 260px; }

  .block { position: absolute; }
  .block--blue   { background: var(--blue);   left: 40px;  top: 0;     width: 90px; height: 36px; }
  .block--yellow { background: var(--yellow); left: 0;     top: 200px; width: 70px; height: 44px; }
  .block--green  { background: var(--leaf-green); left: 520px; top: 300px; width: 100px; height: 54px; }
  .block--forest { background: var(--forest); left: 570px; top: 120px; width: 50px; height: 60px; }
  .block--forest-top { background: var(--forest); left: 0; top: 92px; width: 24px; height: 40px; }

  .photo { position: absolute; border-radius: 40%; }
  .photo--butterfly { left: 170px; top: 26px; width: 90px; height: 48px; background: radial-gradient(#e88a2a, #9a4b14); }
  .photo--grub      { left: 542px; top: 22px; width: 56px; height: 38px; background: radial-gradient(#e3b25c, #b07a2a); }
  .photo--wasp      { left: 190px; top: 200px; width: 70px; height: 44px; background: radial-gradient(#e0a33a, #6b4416); }
  .photo--scorpion  { left: 380px; top: 282px; width: 96px; height: 56px; background: radial-gradient(#6a6a78, #24242c); }

  /* Back */
  .leaf { position: absolute; right: 0; top: 0; width: 110px; height: 56px;
    background: linear-gradient(160deg, #9fd07a, #5aa33e); border-bottom-left-radius: 60px; }
  .ladybird { position: absolute; left: 22px; top: 92px; width: 130px; height: 78px;
    background: radial-gradient(circle at 40% 55%, #c8281e 0 30%, #3a3a2a 31% 40%, #9bcc6a 41% 100%); border-radius: 14px; }

  .contact-name {
    position: absolute; left: 170px; top: 34px;
    font-family: "Comfortaa", sans-serif; font-weight: 700; font-size: 42px;
    color: var(--brown); letter-spacing: 0.5px; white-space: nowrap;
  }
  .contact-line {
    position: absolute; left: 200px; font-family: "Comfortaa", sans-serif;
    font-size: 15px; color: var(--brown); display: flex; align-items: center; gap: 10px;
    white-space: nowrap;
  }
  .contact-line--phone { top: 100px; }
  .contact-line--email { top: 128px; }
  .contact-line .dot { width: 9px; height: 9px; border-radius: 50%; background: #a0301e; }

  .band {
    position: absolute; left: 0; width: 620px; height: 38px;
    display: flex; align-items: center; padding-left: 250px;
    font-family: "Comfortaa", sans-serif; font-size: 18px; color: #fff; letter-spacing: 0.3px;
    white-space: nowrap;
  }
  .band--yellow { top: 176px; background: var(--yellow); }
  .band--green  { top: 220px; background: var(--leaf-green); }
  .band--blue   { top: 264px; background: var(--blue); }
  .band--forest { top: 308px; background: var(--forest); }
</style>
</head>
<body>
<main class="canvas">
  <section class="card card--front" aria-label="Card front">
    <div class="block block--blue"></div>
    <div class="block block--forest-top"></div>
    <div class="block block--yellow"></div>
    <div class="block block--forest"></div>
    <div class="block block--green"></div>

    <span class="bugs-word bugs-word--forest">BUGS</span>
    <span class="bugs-word bugs-word--blue">BUGS</span>
    <span class="bugs-word bugs-word--green">BUGS</span>
    <span class="bugs-word bugs-word--yellow">BUGS</span>

    <div class="photo photo--butterfly" role="img" aria-label="Photo of an orange butterfly"></div>
    <div class="photo photo--grub" role="img" aria-label="Photo of an edible mealworm"></div>
    <div class="photo photo--wasp" role="img" aria-label="Photo of a flying native bee"></div>
    <div class="photo photo--scorpion" role="img" aria-label="Photo of a native scorpion"></div>
  </section>

  <section class="card card--back" aria-label="Card back">
    <div class="leaf" role="img" aria-label="Green leaf photo"></div>
    <div class="ladybird" role="img" aria-label="Illustration of a ladybird on a grass blade with a playful slogan"></div>

    <h1 class="contact-name">wren halloway</h1>
    <p class="contact-line contact-line--phone"><span class="dot"></span>+0 400 218 764</p>
    <p class="contact-line contact-line--email"><span class="dot"></span>contact@wingmeadowlane.com.au</p>

    <div class="band band--yellow">www.critterden.com.au</div>
    <div class="band band--green">www.theamberlocust.com.au</div>
    <div class="band band--blue">www.wingmeadowlane.com.au</div>
    <div class="band band--forest">www.crunchypantryfare.com.au</div>
  </section>
</main>
</body>
</html>
```